We need to design Labels of one of Our Brand QuelaVant Lotion.

The purpose of this product is to keep mosquitoes away.
There are 3 variants of this lotion. So we need 3 designs for the product. These variants details are mentioned below:

1) Mosquito Repellent Lotion with Lavender Fragrance.
2) Mosquito Repellent Lotion with Natural Ingredients.
3) Mosquito Repellent Lotion for kids.

Kindly note the bottle will be WHITE for all the variants. Cap will of the bottle will be with accordance to the color of label. In the picture it is red just for presentation.

Kindly share design of Repellent Lotion with Lavendar Fragrance initially and if we give your positive feedback, then you may add further variants of the design.

The bottle shape is attached along with keylines. Also attaching logo. If there is any other option for logo, you can suggest which we would probably keep our existing logo.

Target Market(s)

B+, B, C+

Industry/Entity Type

Product

Colors
a54499
6b449b

Requirements
Must have
• Mosquito
• 100ml
Nice to have
• Purple color as background
Should not have
• Lavendar flower

```html
<!DOCTYPE html>
<html lang="en">
<head>
<meta charset="utf-8">
<title>QuelaVant Mosquito Repellent Lotion – Lavender Label</title>
<link rel="stylesheet" href="https://fonts.googleapis.com/css2?family=Anton&family=Roboto+Condensed:ital,wght@0,700;1,700&display=swap">
<style>
  :root {
    --page-bg: #ffffff;
    --purple-deep: #4a2a7a;
    --purple: #6b449b;
    --magenta: #a54499;
    --pink-bright: #d2389a;
    --yellow: #ffe21f;
    --white: #ffffff;
    --badge-blue: #1f6fd1;
    --brand-blue: #1d4fb5;
  }
  html, body {
    margin: 0;
    padding: 0;
    width: 1125px;
    height: 1200px;
    overflow: hidden;
    background: var(--page-bg);
  }
  .canvas {
    position: relative;
    width: 1125px;
    height: 1200px;
  }
  .label {
    position: absolute;
    left: 293px;
    top: 80px;
    width: 538px;
    height: 1040px;
  }
  .label-shape {
    position: absolute;
    inset: 0;
    width: 100%;
    height: 100%;
  }
  .badge-new {
    position: absolute;
    left: 22px;
    top: 70px;
    width: 104px;
    height: 104px;
    border-radius: 50%;
    background: var(--badge-blue);
    border: 4px solid var(--white);
    box-sizing: border-box;
    display: flex;
    align-items: center;
    justify-content: center;
    font-family: "Roboto Condensed", sans-serif;
    font-weight: 700;
    font-style: italic;
    font-size: 30px;
    color: var(--white);
    transform: rotate(-12deg);
    z-index: 2;
  }
  .brand {
    position: absolute;
    left: 0;
    right: 0;
    top: 140px;
    text-align: center;
    font-family: "Anton", sans-serif;
    font-size: 104px;
    line-height: 1;
    color: var(--white);
    letter-spacing: 1px;
  }
  .tagline {
    position: absolute;
    left: 0;
    right: 0;
    top: 330px;
    text-align: center;
    font-family: "Roboto Condensed", sans-serif;
    font-weight: 700;
    line-height: 1.12;
  }
  .tagline-main {
    font-style: italic;
    font-size: 42px;
    color: var(--yellow);
    display: block;
  }
  .tagline-variant {
    font-size: 40px;
    color: var(--white);
    display: block;
  }
  .mosquito-art {
    position: absolute;
    left: 169px;
    top: 560px;
    width: 200px;
    height: 210px;
  }
  .volume {
    position: absolute;
    left: 0;
    right: 0;
    top: 940px;
    text-align: center;
    font-family: "Roboto Condensed", sans-serif;
    font-weight: 700;
    font-size: 30px;
    color: var(--white);
  }
</style>
</head>
<body>
<main class="canvas">
  <section class="label">
    <svg class="label-shape" viewBox="0 0 538 1040" xmlns="http://www.w3.org/2000/svg" aria-hidden="true">
      <defs>
        <clipPath id="label-outline">
          <path d="M0,90 Q269,-10 538,90 Q522,330 526,560 Q532,800 538,1010 Q538,1040 508,1040 L30,1040 Q0,1040 0,1010 Q6,800 12,560 Q16,330 0,90 Z"/>
        </clipPath>
        <radialGradient id="label-fill" cx="50%" cy="45%" r="65%">
          <stop offset="0%" stop-color="#7d4fb0"/>
          <stop offset="60%" stop-color="#6b449b"/>
          <stop offset="100%" stop-color="#4a2a7a"/>
        </radialGradient>
        <linearGradient id="v-fill" x1="0" y1="0" x2="0" y2="1">
          <stop offset="0%" stop-color="#d2389a"/>
          <stop offset="100%" stop-color="#a54499"/>
        </linearGradient>
      </defs>
      <g clip-path="url(#label-outline)">
        <rect width="538" height="1040" fill="url(#label-fill)"/>
        <path d="M30,300 L508,300 L269,860 Z" fill="url(#v-fill)"/>
        <rect x="0" y="128" width="538" height="140" fill="var(--brand-blue)" opacity="0.55"/>
      </g>
    </svg>

    <div class="badge-new">NEW</div>
    <div class="brand">QuelaVant</div>

    <p class="tagline">
      <span class="tagline-main">Mosquito Repellent</span>
      <span class="tagline-main">Lotion with</span>
      <span class="tagline-variant">Lavender Fragrance</span>
    </p>

    <svg class="mosquito-art" viewBox="0 0 200 210" role="img" aria-label="Illustration of a mosquito in orange outline">
      <defs>
        <radialGradient id="mosquito-glow" cx="50%" cy="50%" r="50%">
          <stop offset="0%" stop-color="#f5a53c" stop-opacity="0.85"/>
          <stop offset="100%" stop-color="#f5a53c" stop-opacity="0"/>
        </radialGradient>
      </defs>
      <ellipse cx="100" cy="105" rx="100" ry="105" fill="url(#mosquito-glow)"/>
    </svg>

    <div class="volume">100ml</div>
  </section>
</main>
</body>
</html>
```